Website Design For Corben Hub Project

www.corbenhub-example.com.au

As the name suggests i would like to have a design for this website... the website is nothing to do with night life or parties, but it is do everything to do with being online all the time, being available 24/7.

all information needed regarding anything to do with this City and its businesses. so, Basically This will be an online business directory for local businesses. What i am looking for is a website that can display Business listings in a pleasant, lively, friendly, attitude that reflects the towns people, this city boasts with a largest inland city in Australia, and a local university to match, it has its own airport, malls, markets and supermarkets. This website directory/each business layout will be very similar to the ones on www.pelford-direct-example.com.au.

Wagga Wagga has a community of numerous backgrounds, cutlures, creeds and beliefs and religions to be a thriving one.

Therefore, i want the website to reflect its green hills and flowing rivers. The is a advertising point.

An online venue for the local and surrounding bussinesses to be found with a minimum amount of clicks and hassles. Essentially it is a business directory, but not just any directory you see online. I do not want it to look like the fastfind guides or nameline books. this website directory is specific to one location and its bussinesses are particular to that area. I want the website to almost have an emotion for that City, not just an army of black and white ants marching across the page.

Yours colours are you own imagination as long as it is visible and readable by majority of people; its colours are pleasant and not offensive to the eyes: i.e: not too bright, not too dark and depressing.

"corbenhub" is to be included in your website design.

Reason: The deadline has been extended as there are few nice concepts however they need to be a bit more clean in its layout, the color choices are not quite right, as well as the banners need to look more presentable. Thanks

Target Market(s)

The Target Market is Small to Medum Businesses to List their business online and Gen Y and Mums & dads looking for services in the city of Wagga Wagga

Industry/Entity Type

Business Directory

Requirements
Must have
• Search Bar
Social Media Widgets (ChumSpace, Plinko, Pocket sift)
Categories
Sliding Banners
Each Major Category Should have an image or a nice Icon representing the category

```html
<!DOCTYPE html>
<html lang="en">
<head>
<meta charset="utf-8">
<title>Corben Hub</title>
<link rel="stylesheet" href="https://fonts.googleapis.com/css2?family=Arimo:wght@400;700&family=Crimson+Text:wght@400&display=swap">
<style>
:root{
  --teal-dark:#1b4e5b;
  --teal:#235f6d;
  --teal-light:#2e7282;
  --teal-text:#17525f;
  --lime:#8cb31a;
  --lime-dark:#6e9110;
  --sky:#cfe6ee;
  --panel:#e6f0f3;
  --ink:#222;
  --white:#fff;
}
*{margin:0;padding:0;box-sizing:border-box}
html,body{width:800px;height:1200px;overflow:hidden}
body{position:relative;font-family:"Arimo",Arial,sans-serif;color:var(--ink);
  background:linear-gradient(#bcdbe4 0,#d6e9ef 96px,#eef6f8 97px,#f4f9fa 1100px,#e3eff3 1200px)}
.abs{position:absolute}
.page{left:30px;top:18px;width:747px;height:1091px;background:var(--white);border:1px solid #9fb9c1;border-radius:6px;box-shadow:0 0 4px rgba(0,0,0,.15)}
.brand{left:48px;top:34px;display:flex;align-items:center;gap:10px}
.brand-mark{width:34px;height:34px;border-radius:50%;background:var(--sky);border:3px solid #9eb6bd}
.brand-name{font-family:"Crimson Text",Georgia,serif;font-size:38px;color:var(--teal-text);line-height:1}
.search{left:406px;top:35px;width:358px;height:42px;border:1px solid #c5dbe1;border-radius:3px;background:linear-gradient(#f7fbfc,#dcebef)}
.search span{position:absolute;left:80px;top:8px;font-size:15px;color:#555}
.search-btn{position:absolute;right:4px;top:4px;width:38px;height:34px;border-radius:4px;background:linear-gradient(#3a7f8d,#1d5563)}
.hint{left:422px;top:84px;font-size:8.5px;color:var(--teal-text)}
.banner{left:38px;top:100px;width:728px;height:298px;border-radius:8px;overflow:hidden;
  background:radial-gradient(ellipse at 55% 40%,#f5fbfc 0,#d8ecf2 45%,#a9d0dc 100%)}
.banner-photo{position:absolute;left:20px;top:40px;width:420px;height:258px;
  background:linear-gradient(#e9e4df,#b9a79a 60%,#3a3a40);border-radius:120px 120px 0 0;opacity:.85}
.banner h2{position:absolute;left:423px;top:102px;font-weight:400;font-size:24px;color:#111}
.banner p{position:absolute;left:452px;top:151px;width:270px;font-size:14.5px;line-height:24px;color:#111}
.dots{position:absolute;left:616px;top:266px;display:flex}
.dots i{width:17px;height:17px;border-radius:50%;background:#222a30;margin-right:-0.5px;display:block;box-shadow:0 0 0 1px #3a4a50}
.nav{left:38px;top:403px;width:728px;height:36px;border-radius:4px;background:linear-gradient(#2e7180,#1b4e5b);display:flex;padding-left:16px}
.nav a{color:#fff;font-size:12px;text-decoration:none;padding:0 18px;line-height:36px;border-right:1px solid #3e8492}
.nav a.active{background:linear-gradient(#a3c92a,#6e9110);width:69px;text-align:center;padding:0}
.alpha{left:38px;top:444px;width:728px;height:36px;border:1px solid #cfe0e5;border-radius:3px;background:linear-gradient(#fafcfd,#e0edf1);
  font-size:11px;color:#222;display:flex;align-items:center;padding-left:57px}
.alpha b{font-weight:400;width:39px}
.alpha span{width:20px;text-align:center}
.box{left:44px;width:208px;border-radius:4px;color:#fff}
.box-title{position:absolute;left:-9px;top:10px;height:28px;right:0;font-size:14px;line-height:28px;padding-left:46px}
.box-title .icon{position:absolute;left:22px;top:5px;width:18px;height:18px;border-radius:50%;background:#7cc22a;border:1px solid #d9f0a0}
.cats{top:491px;height:252px;background:var(--teal)}
.cats .box-title{background:var(--teal-dark);top:12px}
.cats ul{position:absolute;left:22px;top:46px;list-style:none;font-size:9.5px;line-height:19.2px}
.reloc{top:756px;height:134px;background:var(--lime)}
.reloc .box-title{background:var(--lime-dark);color:#13303a;font-size:12.5px;padding-left:38px;top:14px}
.reloc .box-title .icon{left:14px}
.reloc ul{position:absolute;left:24px;top:47px;list-style:none;font-size:12px;line-height:24px;color:#13303a}
.news{top:902px;height:164px;background:var(--teal)}
.news .box-title{background:var(--teal-dark);padding-left:42px;font-size:14px;top:7px}
.news label{position:absolute;left:16px;font-size:9.5px}
.news .field{position:absolute;left:60px;width:122px;height:24px;border-radius:3px;background:linear-gradient(#fff,#e8eef0)}
.news .subscribe{position:absolute;left:66px;top:118px;width:96px;height:28px;border-radius:3px;background:linear-gradient(#8fb21b,#5f800c);
  font-size:12px;color:#13303a;text-align:center;line-height:28px}
.heading{font-size:14px;color:var(--teal-text)}
.biz{left:314px;top:535px;display:grid;grid-template-columns:161px 153px 130px;font-size:8.5px;line-height:18.3px;color:#222}
.rule{left:295px;top:733px;width:466px;border-top:1px dotted #999}
.results{left:294px;top:773px;font-size:11px}
.listing{left:301px;width:452px;background:var(--panel);border-radius:3px;font-size:9px;line-height:11.5px}
.listing h3{font-weight:400;font-size:11px;color:var(--teal-text)}
.listing .more{color:#2d6f7d}
.wallaby{left:668px;top:1066px;width:132px;height:134px;border-radius:60% 40% 0 0;background:linear-gradient(#b08a68,#7a5a40)}
.social{left:48px;top:1132px;display:flex;gap:6px;font-size:8px;color:var(--teal-text);align-items:center}
.social span{display:flex;flex-direction:column;align-items:center;gap:2px;width:30px}
.social i{width:26px;height:26px;background:var(--teal-light);display:block;border-radius:4px}
.footer-links{left:0;width:970px;top:1139px;text-align:center;font-size:10px;color:#111}
.copy{left:0;width:982px;top:1169px;text-align:center;font-size:9px;color:#111}
</style>
</head>
<body>
<div class="abs page"></div>

<div class="abs brand"><span class="brand-mark"></span><span class="brand-name">Corben Hub</span></div>
<div class="abs search"><span>Search</span>
  <div class="search-btn"><svg width="38" height="34" viewBox="0 0 38 34"><circle cx="17" cy="15" r="7" fill="#bfe3f5" stroke="#fff" stroke-width="2"/><line x1="22" y1="20" x2="29" y2="27" stroke="#fff" stroke-width="3" stroke-linecap="round"/></svg></div>
</div>
<div class="abs hint">Please click on a category and/or business name for more detailed information.</div>

<section class="abs banner">
  <div class="banner-photo" role="img" aria-label="Group of smiling business people in office attire"></div>
  <h2>Lorem ipsum dolor sit amet</h2>
  <p>Lorem ipsum dolor sit amet, consectetuer adipiscing elit. Nam nibh. Nunc varius facilisis eros. Sed erat.</p>
  <div class="dots"><i></i><i></i><i></i><i></i></div>
</section>

<nav class="abs nav"><a class="active" href="#">Home</a><a href="#">About Corben Hub</a><a href="#">Gallery</a><a href="#" style="border:0">Contact us</a></nav>

<div class="abs alpha"><b>0-9</b><span>A</span><span>B</span><span>C</span><span>D</span><span>E</span><span>F</span><span>G</span><span>H</span><span>I</span><span>J</span><span>K</span><span>L</span><span>M</span><span>N</span><span>O</span><span>P</span><span>Q</span><span>R</span><span>S</span><span>T</span><span>U</span><span>V</span><span>W</span><span>X</span><span>Y</span><span>Z</span></div>

<aside class="abs box cats">
  <div class="box-title"><span class="icon"></span>Catagories</div>
  <ul>
    <li>&gt;&gt;&nbsp;&nbsp; Education</li><li>&gt;&gt;&nbsp;&nbsp;Healthcare</li><li>&gt;&gt;&nbsp;&nbsp;Sport</li><li>&gt;&gt;&nbsp;&nbsp;Migration</li><li>&gt;&gt;&nbsp;&nbsp;Accommodation</li><li>&gt;&gt;&nbsp;&nbsp;Tourism</li><li>&gt;&gt;&nbsp;&nbsp;Arts &amp; Culture</li><li>&gt;&gt;&nbsp;&nbsp;Case Studies</li><li>&gt;&gt;&nbsp;&nbsp;Relocation consultant</li><li>&gt;&gt;&nbsp;&nbsp;Community Services</li>
  </ul>
</aside>

<aside class="abs box reloc">
  <div class="box-title"><span class="icon"></span>Reloacation Consultant</div>
  <ul><li><small>&gt;&gt;</small> Work</li><li><small>&gt;&gt;</small> Visit</li><li><small>&gt;&gt;</small> Invest</li></ul>
</aside>

<aside class="abs box news">
  <div class="box-title">Newsletter</div>
  <label style="top:56px">Name&nbsp; :</label><div class="field" style="top:49px"></div>
  <label style="top:88px">Email&nbsp; :</label><div class="field" style="top:82px"></div>
  <div class="subscribe">Subscribe</div>
</aside>

<h2 class="abs heading" style="left:290px;top:505px;font-weight:400">Business Searches</h2>
<div class="abs biz">
  <span>&gt; CCTV</span><span>&gt; Spa &amp; Salons</span><span>&gt; Jewelry &amp; Watches</span>
  <span>&gt; Water Jet Pumps</span><span>&gt; Hospitals</span><span>&gt; Interior Decorations</span>
  <span>&gt; Movie theaters</span><span>&gt; Furnitures</span><span>&gt; Life Insurance</span>
  <span>&gt; Doctors</span><span>&gt; Event Planners</span><span>&gt; House Cleaning</span>
  <span>&gt; Diesel Generator</span><span>&gt; Banks</span><span>&gt; Doctors</span>
  <span>&gt; Out Door Advertising</span><span>&gt; Fire Alarm</span><span>&gt; Home Appliances</span>
  <span>&gt; Bars &amp; Clubs</span><span>&gt; Accessories</span><span>&gt; Pest Control</span>
  <span>&gt; Movie theaters</span><span>&gt; Detective Agencies</span><span>&gt; Security Systems</span>
  <span>&gt; Bars &amp; Clubs</span><span>&gt; Water Jet Pumps</span><span>&gt; Industrial Chemicals</span>
  <span>&gt; Travel Agents</span><span>&gt; Out Door Advertising</span><span>&gt; Packaging Material</span>
</div>
<div class="abs rule"></div>
<h2 class="abs heading" style="left:292px;top:744px;font-weight:400">Listings</h2>
<div class="abs results">Results 1 - 9 of 9</div>

<article class="abs listing" style="top:800px;height:120px;padding:21px 13px">
  <h3>Bellino Cafe Featured</h3>
  <p style="margin-top:10px">All of our Pastizzi's and Pastas are home made right here on the premises.<br>Our coffee's are created by our Baristas and we only use the best 'Casa Forte' 100 % Arabica blend<br>&nbsp;coffee Beans.</p>
  <p class="more" style="margin-top:11px">We are open from early (9ish) to late (someti ...</p>
</article>

<article class="abs listing" style="top:932px;height:120px;padding:19px 19px">
  <h3>Hypnotherapist, NLP Master Practitioner Featured</h3>
  <h3 style="margin-top:9px">Change your mind, change your weight!</h3>
  <p style="margin:11px 0 0 16px">Do you get disheartened about your eating habits and your weight?<br>Do you find it difficult to say no to second helpings?<br>Are you unable to lose those last few kilos?...</p>
</article>

<div class="abs wallaby" role="img" aria-label="Wallaby standing at the page corner"></div>

<div class="abs social">
  <span><i></i>ChumSpace</span><span><i></i>Plinko</span><span><i></i>Workweave</span><span><i></i>Postloft</span>
</div>
<div class="abs footer-links">About Us | Contact Us | Privacy Policy | Terms of Service | Site map</div>
<div class="abs copy">© 2011 CorbenHub, All Rights Reserved</div>
</body>
</html>
```